Lowen Academy

I need different posters for a high school that displays positive messaging and the school's core values.
Want the design to look sleek for high school aged children

1. Poster #1
CORE VALUES:
• RESPECT
• RESPONSIBILITY
• LEADERSHIP
• PRIDE
• COMMUNITY

2. Acronym posters for the school
Empathy
Zeal
Respect
Aspire

3. additional acronym poster
Encourage
Zenith
Relationships
Accountability

```html
<!DOCTYPE html>
<html lang="en">
<head>
<meta charset="utf-8">
<title>Lowen Academy — Core Values Posters</title>
<link rel="stylesheet" href="https://fonts.googleapis.com/css2?family=Bebas+Neue&family=Montserrat:wght@400&display=swap">
<style>
  :root {
    --backdrop: #bcbcbe;
    --navy: #23205e;
    --purple: #3f2470;
    --white: #f4f4f2;
    --sky: #1ea3dc;
    --lemon: #e3e327;
    --lime: #7dc243;
    --tangerine: #f0891e;
  }
  html, body {
    margin: 0;
    padding: 0;
    width: 1200px;
    height: 882px;
    overflow: hidden;
    background: var(--backdrop);
  }
  .canvas {
    position: relative;
    width: 1200px;
    height: 882px;
  }
  .poster {
    position: absolute;
    top: 154px;
    width: 424px;
    height: 591px;
    overflow: hidden;
    box-shadow: 0 1px 3px rgba(0,0,0,0.25);
    font-family: "Bebas Neue", "Oswald", sans-serif;
    color: var(--white);
  }
  .poster--values { left: 121px; background: var(--navy); }
  .poster--acronym { left: 636px; background: var(--purple); }

  .eyebrow {
    position: absolute;
    left: 33px;
    top: 136px;
    transform: rotate(-90deg);
    transform-origin: left top;
    font-family: "Montserrat", sans-serif;
    font-size: 8px;
    letter-spacing: 2.4px;
    white-space: nowrap;
  }
  .art-bulb {
    position: absolute;
    left: 80px;
    top: 0;
    width: 265px;
    height: 282px;
    background: radial-gradient(ellipse 45% 40% at 50% 52%, var(--lemon) 0 70%, transparent 72%),
                linear-gradient(var(--navy), var(--navy));
  }
  .value-list {
    position: absolute;
    left: 38px;
    top: 322px;
    margin: 0;
    padding: 0;
    list-style: none;
    font-size: 44px;
    line-height: 48px;
  }
  .value-list .accent { color: var(--sky); }
  .art-pattern {
    position: absolute;
    left: 318px;
    top: 329px;
    width: 68px;
    height: 222px;
    background: linear-gradient(135deg, var(--white) 0 50%, var(--sky) 50% 100%);
  }

  .dot {
    position: absolute;
    border-radius: 50%;
  }
  .dot--lime { left: 32px; top: 19px; width: 92px; height: 92px; background: var(--lime); }
  .dot--tangerine { left: 300px; top: 478px; width: 94px; height: 94px; background: var(--tangerine); }
  .headline {
    position: absolute;
    margin: 0;
    font-weight: 400;
    font-size: 44px;
    line-height: 43px;
  }
  .headline--top { right: 37px; top: 30px; text-align: right; }
  .headline--bottom { left: 40px; top: 465px; }
  .art-hands {
    position: absolute;
    left: 56px;
    top: 137px;
    width: 312px;
    height: 312px;
    border-radius: 50%;
    background: radial-gradient(circle, var(--lemon) 0 55%, #c9dc3a 55% 80%, var(--lime) 80% 100%);
  }
</style>
</head>
<body>
<main class="canvas">
  <section class="poster poster--values" aria-label="Core values poster">
    <div class="eyebrow">CORE VALUES</div>
    <div class="art-bulb" role="img" aria-label="Illustration of a glowing yellow light bulb with white rays"></div>
    <ul class="value-list">
      <li>Respect</li>
      <li class="accent">Responsibility</li>
      <li>Leadership</li>
      <li class="accent">Pride</li>
      <li>Community</li>
    </ul>
    <div class="art-pattern" role="img" aria-label="Column of white and blue triangle pattern"></div>
  </section>

  <section class="poster poster--acronym" aria-label="Acronym poster">
    <span class="dot dot--lime"></span>
    <h2 class="headline headline--top">Aspire<br>Empathy</h2>
    <div class="art-hands" role="img" aria-label="Illustration of two orange hands reaching toward each other over a glowing green and yellow circle"></div>
    <h2 class="headline headline--bottom">Zeal<br>Respect</h2>
    <span class="dot dot--tangerine"></span>
  </section>
</main>
</body>
</html>
```